Corporate Brightfen business cards to be handed to investor, bankers etc. Needs to have a young feel

I need business cards designed for a technology company that provides uber-like rapid response on the security industry. I would like it simple but very cool and tasteful. See attached documents for artwork and colours to be used. Cut sheet describes business model. Card stock should be thicker than normal. I would like the one side to be just the art and the other to have the contact info with maybe the pin somewhere.

Target Market(s)

Investors

Industry/Entity Type

Business

Contact Information for Business Card

Would like the logo attached on one side with name address and other info on the other side.

Font styles to use
Other font styles liked:
• See existing logo

Colors
6b449b
886aae
e4daeb
ffffff

Requirements
Must have
• Name: Dorian Felkatsis
• Address: 47 Larkfield Avenue, Toronto, On, M6K2B7
• Tel: 416-7291846
• Email: rolo@brightfen.io
Nice to have
• See logo colours

```html
<!DOCTYPE html>
<html lang="en">
<head>
<meta charset="utf-8">
<title>Brightfen Business Cards</title>
<link rel="stylesheet" href="https://fonts.googleapis.com/css2?family=Mulish:wght@400;500&display=swap">
<style>
  :root {
    --canvas: #ecebee;
    --card-white: #ffffff;
    --card-black: #1e1c1d;
    --brand-purple: #7d5aa8;
    --ink: #1b1a1b;
    --text-light: #ffffff;
    --mark-grey: #c9c9cb;
  }
  * { margin: 0; padding: 0; box-sizing: border-box; }
  html, body {
    width: 1200px; height: 900px; overflow: hidden;
    background: var(--canvas);
    font-family: "Mulish", sans-serif;
  }
  .stage { position: relative; width: 1200px; height: 900px; }

  .card { position: absolute; box-shadow: 0 8px 24px rgba(0,0,0,.18); overflow: hidden; }

  .card-front {
    left: 78px; top: 34px; width: 588px; height: 364px;
    background: var(--card-white);
  }
  .card-front .shapes { position: absolute; inset: 0; }
  .wordmark {
    position: absolute; left: 0; right: 0; top: 78px;
    display: flex; justify-content: center; align-items: center; gap: 14px;
    color: var(--ink); font-weight: 400; font-size: 62px; letter-spacing: -1px;
  }
  .wordmark-dot {
    width: 30px; height: 30px; border-radius: 50%;
    background: var(--brand-purple); margin-top: 12px;
  }
  .holder-name {
    position: absolute; right: 36px; top: 252px;
    color: var(--text-light); font-size: 20px; font-weight: 500;
  }
  .contact {
    position: absolute; color: var(--text-light); font-size: 15px; line-height: 22px;
  }
  .contact-address { left: 30px; top: 296px; }
  .contact-address .line { display: flex; align-items: center; gap: 6px; }
  .contact-address .line + .line { padding-left: 18px; }
  .contact-reach { right: 36px; top: 299px; text-align: right; }
  .contact-reach .line { display: flex; align-items: center; justify-content: flex-end; gap: 8px; }
  .icon { width: 13px; height: 13px; fill: var(--text-light); flex: none; }

  .card-back {
    left: 388px; top: 505px; width: 566px; height: 352px;
    background: var(--card-black);
    display: flex; align-items: center; justify-content: center; gap: 14px;
  }
  .back-dot { width: 34px; height: 34px; border-radius: 50%; background: var(--mark-grey); }
  .back-name { color: var(--mark-grey); font-size: 44px; font-weight: 400; letter-spacing: -0.5px; }
</style>
</head>
<body>
<main class="stage">
  <section class="card card-front" aria-label="Business card front">
    <svg class="shapes" width="588" height="364" viewBox="0 0 588 364">
      <polygon fill="var(--brand-purple)" points="0,210 352,210 333,236 0,236"/>
      <polygon fill="var(--card-black)" points="362,202 588,202 588,364 0,364 0,239 337,239"/>
    </svg>
    <div class="wordmark"><span class="wordmark-dot"></span><span>brightfen</span></div>
    <p class="holder-name">Dorian Felkatsis</p>
    <div class="contact contact-address">
      <p class="line">
        <svg class="icon" viewBox="0 0 24 24"><path d="M12 1a8 8 0 0 0-8 8c0 6 8 14 8 14s8-8 8-14a8 8 0 0 0-8-8zm0 11a3 3 0 1 1 0-6 3 3 0 0 1 0 6z"/></svg>
        47 Larkfield Avenue,
      </p>
      <p class="line">Toronto, On, M6K2B7</p>
    </div>
    <div class="contact contact-reach">
      <p class="line">416-7291846
        <svg class="icon" viewBox="0 0 24 24"><path d="M6.6 10.8a15 15 0 0 0 6.6 6.6l2.2-2.2c.3-.3.7-.4 1-.2 1.1.4 2.3.6 3.6.6.6 0 1 .4 1 1V20c0 .6-.4 1-1 1A17 17 0 0 1 3 4c0-.6.4-1 1-1h3.5c.6 0 1 .4 1 1 0 1.3.2 2.5.6 3.6.1.3 0 .7-.2 1z"/></svg>
      </p>
      <p class="line">rolo@brightfen.io
        <svg class="icon" viewBox="0 0 24 24"><path d="M2 5h20v14H2z M2 5l10 8 10-8" fill="var(--text-light)" stroke="var(--card-black)" stroke-width="1.6"/></svg>
      </p>
    </div>
  </section>

  <section class="card card-back" aria-label="Business card back">
    <span class="back-dot"></span>
    <span class="back-name">brightfen</span>
  </section>
</main>
</body>
</html>
```